Security and Automation Company based in Texas and needs logo design also

Looking for a new logo design for our company - we are based in Texas and specialize in camera, security and home automation - We do want the main company name(Brightline Guard and Controls of Texas) with our parent company in small letters below (a Veloran Partners, LLC Company) and our License number needs to be included in the design - K74836 - Darker shades of blue preferred

Target Market(s)

We work with everyone from home to large corporate - so clean design would be helpful

Industry/Entity Type

It Company

Contact Information for Business Card

PO Box 4719
Cedar Hollow, Texas 75961
Leave a spot for the phone number and email address

Logo Text

Brightline Guard and Controls of Texas/a Veloran Partners Company/K74836

Font styles to use
Sans Serif

Colors
0255a3

```html
<!DOCTYPE html>
<html lang="en">
<head>
<meta charset="utf-8">
<title>Brightline Guard and Controls of Texas – Business Card</title>
<link rel="stylesheet" href="https://fonts.googleapis.com/css2?family=Arimo:wght@400;700&family=Roboto+Condensed:wght@400&display=swap">
<style>
  :root {
    --brand-blue: #0255a3;
    --faint-blue: #3b7cbd;
    --paper: #ffffff;
    --stage: #cccccc;
    --ink: #111111;
  }
  * { margin: 0; padding: 0; box-sizing: border-box; }
  html, body { width: 1200px; height: 900px; overflow: hidden; background: var(--stage); }
  .canvas { position: relative; width: 1200px; height: 900px; font-family: "Arimo", Arial, sans-serif; }

  .card { position: absolute; left: 271px; width: 656px; height: 376px; border-radius: 7px; overflow: hidden; }

  /* front */
  .card-front { top: 45px; background: var(--paper); }
  .front-band { position: absolute; left: 0; right: 0; top: 181px; bottom: 0; background: var(--brand-blue); }
  .brand-mark {
    position: absolute; left: 397px; top: 34px; width: 220px; height: 220px; border-radius: 50%;
    background: var(--brand-blue); border: 3px solid var(--ink); box-shadow: 0 0 0 5px var(--paper) inset;
  }
  .brand-name {
    position: absolute; left: 28px; top: 78px; width: 340px;
    color: var(--brand-blue); font-weight: 700; font-size: 21px; line-height: 1.25;
  }
  .contact-list { position: absolute; left: 0; top: 0; list-style: none; color: var(--paper); font-weight: 700; font-size: 15.5px; }
  .contact-item { position: absolute; left: 47px; white-space: nowrap; line-height: 18px; }
  .contact-icon { position: absolute; left: -21px; top: 1px; width: 17px; height: 17px; }
  .person { position: absolute; left: 365px; top: 283px; color: var(--paper); }
  .person-name { font-weight: 700; font-size: 24.5px; letter-spacing: 0.3px; line-height: 1; }
  .person-title { font-size: 22px; line-height: 1.1; margin-top: 2px; }

  /* back */
  .card-back { top: 501px; background: var(--brand-blue); }
  .back-disc { position: absolute; left: 351px; top: -4px; width: 308px; height: 308px; border-radius: 50%; background: var(--faint-blue); }
  .service { position: absolute; display: flex; align-items: center; gap: 13px; color: var(--paper);
    font-family: "Roboto Condensed", "Arial Narrow", sans-serif; font-size: 20px; }
  .service-badge { width: 44px; height: 44px; border-radius: 50%; background: var(--paper);
    display: flex; align-items: center; justify-content: center; flex: none; }
  .service-badge svg { width: 22px; height: 22px; fill: var(--brand-blue); }
  .service-label { margin-top: -14px; }
</style>
</head>
<body>
<div class="canvas">

  <section class="card card-front">
    <div class="front-band"></div>
    <p class="brand-name">Brightline Guard and Controls of Texas</p>
    <div class="brand-mark"></div>

    <ul class="contact-list">
      <li class="contact-item" style="top:222px">
        <svg class="contact-icon" viewBox="0 0 20 20"><circle cx="10" cy="10" r="10" fill="#fff"/><path d="M6 5l2 0 1 3-1.3 1a7 7 0 0 0 3.3 3.3l1-1.3 3 1 0 2c0 .7-.6 1-1.2 1A9 9 0 0 1 5 6.2C5 5.6 5.3 5 6 5z" fill="#0255a3"/></svg>
        012345 6789</li>
      <li class="contact-item" style="top:248px">
        <svg class="contact-icon" viewBox="0 0 20 20"><rect x="6" y="3" width="9" height="16" rx="1.5" fill="none" stroke="#fff" stroke-width="1.6"/><rect x="8" y="5.5" width="5" height="5" fill="#fff"/></svg>
        +012345 6789</li>
      <li class="contact-item" style="top:276px">
        <svg class="contact-icon" viewBox="0 0 20 20"><rect x="1" y="4" width="16" height="11" fill="none" stroke="#fff" stroke-width="1.5"/><path d="M1 4l8 6 8-6" fill="none" stroke="#fff" stroke-width="1.5"/></svg>
        email address</li>
      <li class="contact-item" style="top:299px">
        <svg class="contact-icon" viewBox="0 0 20 20"><circle cx="10" cy="10" r="8" fill="none" stroke="#fff" stroke-width="1.5"/><ellipse cx="10" cy="10" rx="3.5" ry="8" fill="none" stroke="#fff" stroke-width="1.3"/><path d="M2 10h16M3.5 6h13M3.5 14h13" stroke="#fff" stroke-width="1.2"/></svg>
        website here</li>
      <li class="contact-item" style="top:322px">
        <svg class="contact-icon" viewBox="0 0 20 20"><path d="M10 2L1 10h3v8h4.5v-5h3v5H16v-8h3z" fill="#fff"/></svg>
        PO Box 4719<br>Cedar Hollow, Texas 75961</li>
    </ul>

    <div class="person">
      <p class="person-name">MR. BRIGHTLINE GUARD</p>
      <p class="person-title">Director</p>
    </div>
  </section>

  <section class="card card-back">
    <div class="back-disc"></div>

    <div class="service" style="left:37px;top:53px">
      <span class="service-badge"><svg viewBox="0 0 24 24"><path d="M12 6C6 6 2 12 2 12s4 6 10 6 10-6 10-6-4-6-10-6zm0 9.5A3.5 3.5 0 1 1 12 8.5a3.5 3.5 0 0 1 0 7z"/></svg></span>
      <span class="service-label">Your Service</span></div>
    <div class="service" style="left:92px;top:96px">
      <span class="service-badge"><svg viewBox="0 0 24 24"><path d="M12 3L2 12h3v8h5v-5h4v5h5v-8h3z"/></svg></span>
      <span class="service-label">Your Service</span></div>
    <div class="service" style="left:150px;top:140px">
      <span class="service-badge"><svg viewBox="0 0 24 24"><path d="M12 2l3 7h7l-5.6 4.3 2.1 7.2L12 16.3 5.5 20.5l2.1-7.2L2 9h7z"/></svg></span>
      <span class="service-label">Your Service</span></div>
    <div class="service" style="left:207px;top:188px">
      <span class="service-badge"><svg viewBox="0 0 24 24"><path d="M3 7h4l2-3h6l2 3h4v13H3zm9 10a4 4 0 1 0 0-8 4 4 0 0 0 0 8zm0-2a2 2 0 1 1 0-4 2 2 0 0 1 0 4z"/></svg></span>
      <span class="service-label">Your Service</span></div>
    <div class="service" style="left:270px;top:236px">
      <span class="service-badge"><svg viewBox="0 0 24 24"><path d="M2 7h14v10H2zm14 4l6-4v10l-6-4z"/></svg></span>
      <span class="service-label">Your Service</span></div>
    <div class="service" style="left:335px;top:289px">
      <span class="service-badge"><svg viewBox="0 0 24 24"><text x="12" y="20" text-anchor="middle" font-family="Arimo, Arial, sans-serif" font-weight="700" font-size="21">$</text></svg></span>
      <span class="service-label">Your Service</span></div>
  </section>

</div>
</body>
</html>
```